Menu board for car wash

I need to have a menu board designed for my car wash. I would like for it to replicate the attached graphics of other menu boards other car washes are using. The menu board will be printed locally and be cut out with a router. I want the menu board to clearly show what they are buying and promote buying the top wash package. I also want "the Works" package to show that you can buy a monthly plan for $23.95 and receive this wash unlimited times per month. I have attached my menu that i have now (Kellingtonmenu). I would like for this new menu to have the same wording as the previous menu for the wash packages. The only addition is a new wash package "Summit Sparkle" which is now the top wash package. The new menu i would like to have going vertical and I would like my logo on the top. This menu would be 8' high and 4'wide.

Target Market(s)

Looking to have this menu be attractive and inviting. The top package should stand out the most and the lowest package should barely be noticeable ( basic wash)
I am targeting customer from the ages of 16-65 years old.

Industry/Entity Type

Automotive

Font styles to use
Serif
Sans Serif
Decorative
Other font styles liked:
• any font that flows with the design

Colors

Designer to choose colors to be used in the design.

Requirements
Must have
• This menu will be die cut out. It must fit in a 8' x 4' vertical art board.
• The wash packages will need to go from top to bottom
• They should be listed as follows
• Summit Sparkle $18
• The Works $13 ( also add Unlimited for $23.95)
• Deluxe $10
• Basic $8
• I would like to have an extras section also added just like my original menu. This can be at the bottom of the menu If you have any cool graphics that go with my theme or washes please feel free.
• The new Summit Sparkle wash will have the following included:
• Presoak
• Bug Treatment
• wheel cleaner
• Undercarriage wash
• Triple Foam Polish
• Clear Coat Protectant
• Hot Wax Treatment ( you can use graphic that is on my old menu for this item)
• Tire Shine ( You can use the Storm Glide logo)
• Hand Towel Dried
Nice to have
• Incorporate my business hours also on the menu
• the hours are:
• Monday-Saturday 8:00 Am-6:00 Pm
• Sunday 8:00 Am-5:00 Pm
• Weather may effect these hours
Should not have
• Text should be clearly visable so anyone car read it easily

```html
<!DOCTYPE html>
<html lang="en">
<head>
<meta charset="utf-8">
<title>Kellington Car Wash Menu Board</title>
<link rel="stylesheet" href="https://fonts.googleapis.com/css2?family=Lobster&family=Bangers&family=Roboto+Condensed:wght@400;700;900&display=swap">
<style>
  :root{
    --backdrop:#8c8c8c;
    --red:#e3322a;
    --red-dark:#b21f1a;
    --yellow:#ffd21f;
    --cream:#fff6d2;
    --white:#ffffff;
    --ink:#1d1d1d;
    --blue:#1f4e9e;
    --sky:#7cc3ea;
    --orange:#f2a23a;
  }
  *{box-sizing:border-box;margin:0;padding:0}
  html,body{width:865px;height:1200px;overflow:hidden}
  body{background:var(--backdrop);font-family:"Roboto Condensed",Arial,sans-serif;position:relative}
  .panel{position:absolute;z-index:2;background:var(--red);border:8px solid var(--yellow);border-radius:24px;box-shadow:0 0 0 4px var(--red-dark)}

  .brand{left:230px;top:28px;width:405px;height:205px;background:var(--yellow);border-color:var(--red);box-shadow:0 0 0 4px var(--yellow);
    display:flex;flex-direction:column;align-items:center;justify-content:center;text-align:center}
  .brand-name{font-family:"Lobster",cursive;color:var(--red);font-size:46px;line-height:1}
  .brand-name.big{font-size:78px;margin-top:6px}

  .heading{font-family:"Bangers",cursive;color:var(--yellow);letter-spacing:2px;line-height:1}
  .script{font-family:"Lobster",cursive;color:var(--yellow);line-height:1}

  .feature-list{list-style:none;color:var(--yellow);font-weight:700}
  .feature-list li{position:relative;padding-left:28px;line-height:1.25}
  .feature-list li::before{content:"";position:absolute;left:4px;top:.22em;width:8px;height:14px;border:solid var(--yellow);border-width:0 4px 4px 0;transform:rotate(40deg)}

  .price{position:absolute;border-radius:50%;display:flex;align-items:center;justify-content:center;font-weight:900}

  /* Summit Sparkle */
  .summit{left:70px;top:250px;width:750px;height:295px}
  .summit .heading{position:absolute;left:30px;top:14px;font-size:66px}
  .summit .feature-list{position:absolute;top:92px;font-size:24px}
  .summit .col-a{left:40px}
  .summit .col-b{left:310px}
  .summit .price{right:22px;top:82px;width:145px;height:145px;background:var(--white);border:8px solid var(--yellow);color:var(--red);font-size:56px}
  .extra{position:absolute;bottom:18px;display:flex;align-items:center;gap:10px;color:var(--cream);font-weight:900;font-size:20px}
  .extra.wax{left:40px}
  .wax-badge{width:44px;height:30px;border-radius:50%;background:var(--yellow)}
  .extra.tire{left:420px;flex-direction:column;align-items:flex-start;gap:2px}
  .storm{display:flex;align-items:center;gap:8px;color:var(--white);font-size:22px;font-weight:900}
  .storm-mark{width:18px;height:18px;background:var(--ink)}
  .tire-label{color:var(--ink);font-size:22px;letter-spacing:1px}

  /* The Works */
  .works{left:70px;top:565px;width:620px;height:180px}
  .works .heading{position:absolute;left:28px;top:12px;font-size:52px}
  .works .plan{position:absolute;left:30px;top:70px;color:var(--cream);font-size:22px;font-weight:700;line-height:1.2}
  .works .plan strong{color:var(--yellow);font-weight:900}
  .works .price{right:28px;top:28px;width:110px;height:110px;background:var(--red-dark);border:6px solid var(--white);color:var(--white);font-size:44px}

  /* Deluxe */
  .deluxe{left:70px;top:765px;width:630px;height:175px}
  .deluxe .script{position:absolute;left:28px;top:8px;font-size:50px}
  .deluxe .price{left:200px;top:12px;width:62px;height:62px;background:var(--yellow);color:var(--red);font-size:26px}
  .deluxe .feature-list{position:absolute;top:76px;font-size:21px}
  .deluxe .feature-list li{line-height:1.2}
  .deluxe .col-a{left:36px}
  .deluxe .col-b{left:280px}

  /* Basic */
  .basic{left:70px;top:960px;width:600px;height:95px}
  .basic .script{position:absolute;left:28px;top:14px;font-size:46px}
  .basic .feature-list{position:absolute;left:200px;top:6px;font-size:18px}
  .basic .feature-list li{line-height:1.15}
  .basic .price{right:40px;top:11px;width:56px;height:56px;background:var(--red-dark);border:4px solid var(--yellow);color:var(--white);font-size:24px}

  /* Attendant art, sits behind the panels */
  .attendant{position:absolute;z-index:1;left:600px;top:560px;width:230px;height:600px;border-radius:30px;
    background:linear-gradient(180deg,var(--orange) 0%,var(--sky) 55%,var(--blue) 100%)}

  /* Hours */
  .hours{position:absolute;z-index:2;left:255px;top:1070px;width:330px;height:115px;background:var(--blue);border:4px solid var(--white);border-radius:10px;color:var(--white);text-align:center;padding-top:8px}
  .hours h2{font-size:26px;font-weight:900;letter-spacing:1px}
  .hours dl{display:grid;grid-template-columns:auto auto;justify-content:center;column-gap:18px;font-size:16px;text-align:left;margin-top:4px}
  .hours dd{font-weight:700}
  .hours p{font-size:13px;margin-top:4px}
</style>
</head>
<body>
  <header class="panel brand">
    <span class="brand-name">Kellington</span>
    <span class="brand-name big">Car Wash</span>
  </header>

  <section class="panel summit">
    <h2 class="heading">SUMMIT SPARKLE</h2>
    <ul class="feature-list col-a">
      <li>Presoak</li><li>Bug Treatment</li><li>wheel cleaner</li><li>Undercarriage wash</li>
    </ul>
    <ul class="feature-list col-b">
      <li>Triple Foam Polish</li><li>Clear Coat Protectant</li><li>Hand Towel Dried</li>
    </ul>
    <div class="extra wax"><span class="wax-badge"></span>Hot Wax Treatment</div>
    <div class="extra tire">
      <span class="storm"><span class="storm-mark"></span>Storm Glide</span>
      <span class="tire-label">TIRE SHINE</span>
    </div>
    <div class="price">$18</div>
  </section>

  <div class="attendant" role="img" aria-label="Car wash attendant in blue overalls holding a pressure washer, with a water splash at his feet"></div>

  <section class="panel works">
    <h2 class="heading">THE WORKS</h2>
    <p class="plan">Buy A Monthly Plan For <strong>$23.95</strong><br>and receive this wash<br><strong>UNLIMITED TIMES PER MONTH</strong></p>
    <div class="price">$13</div>
  </section>

  <section class="panel deluxe">
    <h2 class="script">Deluxe</h2>
    <div class="price">$10</div>
    <ul class="feature-list col-a">
      <li>Presoak</li><li>wheel cleaner</li><li>Undercarriage wash</li>
    </ul>
    <ul class="feature-list col-b">
      <li>Triple Foam Polish</li><li>Clear Coat</li><li>Hand Towel Dry</li>
    </ul>
  </section>

  <section class="panel basic">
    <h2 class="script">Basic</h2>
    <ul class="feature-list">
      <li>Presoak</li><li>Wash</li><li>Dry</li>
    </ul>
    <div class="price">$8</div>
  </section>

  <aside class="hours">
    <h2>BUSINESS HOURS</h2>
    <dl>
      <dt>Monday-Saturday</dt><dd>8:00 Am-6:00 Pm</dd>
      <dt>Sunday</dt><dd>8:00 Am-5:00 Pm</dd>
    </dl>
    <p>(Weather may effect these hours)</p>
  </aside>
</body>
</html>
```